Create a Brochure Design for Brantley Homecare

Brantley Homecare is a subsidiary of the Brantley Care Group. This brochure is specifically for the Brantley Homecare company and brand. Create a 3 panel, A4, front and back, tri-fold brochure. This brochure will be a way to introduce our Homecare services to the community, prospective clients, and various referral partners. The brochure must be eye catching, unique in its deliverables and demonstrate both attention to detail and comfort. Our organization is sophisticated and built around warmth, care and individualized personal attention. The most important aspect of this design is to focus on creating a nurturing, warm, and inviting feel where you would want to have a Nurse or Nurse’s Aide in your own home or a loved one’s home.

I am open to the creativity of the designer to develop something based on the above criteria; however I would like the design to work well with the existing collateral material. What I mean by that is that while I want everything to have its own personality and stand out as its own brand representative, I still need to be able to tell that the overall design concept stays stylistically inside of the same ‘family’ of existing designed material. Because of this, below I would like for the designer to pull inspiration from the link to our website (Located below) as well as from the attachment of our recently refreshed business cards (Attached). This should allow each design to be unique and creative, while still staying inside of a framework and the feel/style that I am looking for.

Finally, I want all the designers to understand that this brochure design is for a private, in home, healthcare company where we are responsible for providing personalized care for a culturally and ethnically diverse make-up clientele of all ages. The photos that are used must represent an image of warmth, care, and a positive interaction between client and caregiver.

Look under the Brantley Homecare tab at www.brantleycaregroup-example.net

Industry/Entity Type

Healthcare

Requirements
Must have
• • The Brantley Homecare company logo must be included.

```html
<!DOCTYPE html>
<html lang="en">
<head>
<meta charset="utf-8">
<title>Brantley Homecare – Tri-fold Brochure</title>
<link rel="stylesheet" href="https://fonts.googleapis.com/css2?family=Comfortaa:wght@400;700&family=Questrial&display=swap">
<style>
  :root {
    --charcoal: #3b3b3d;
    --charcoal-deep: #2f2f31;
    --salmon: #e9876f;
    --teal: #1e5a5c;
    --paper: #ffffff;
    --body-light: #e6e6e6;
    --stage: #e9e7e4;
    --photo-warm-a: #7a5a45;
    --photo-warm-b: #c9b8a6;
    --photo-cool-a: #d9dde0;
    --photo-cool-b: #9aa6ae;
    --photo-dark-a: #2a1f1a;
    --photo-dark-b: #6d5445;
  }
  * { box-sizing: border-box; margin: 0; padding: 0; }
  html, body { width: 1200px; height: 900px; overflow: hidden; }
  body {
    background: var(--stage);
    font-family: "Questrial", "Century Gothic", sans-serif;
    position: relative;
  }
  .spread {
    position: absolute;
    left: 300px;
    width: 600px;
    height: 400px;
    display: flex;
    box-shadow: 0 2px 8px rgba(0,0,0,.18);
  }
  .spread--inside { top: 40px; }
  .spread--outside { top: 460px; }
  .panel {
    width: 200px;
    height: 100%;
    display: flex;
    flex-direction: column;
    overflow: hidden;
    background: var(--charcoal);
    color: var(--body-light);
  }
  .photo { flex-shrink: 0; width: 100%; }
  .photo--warm { background: linear-gradient(135deg, var(--photo-warm-a), var(--photo-warm-b)); }
  .photo--cool { background: linear-gradient(135deg, var(--photo-cool-a), var(--photo-cool-b)); }
  .photo--portrait { background: radial-gradient(ellipse at 60% 45%, var(--photo-dark-b), var(--photo-dark-a) 75%); }
  .copy {
    font-size: 6.2px;
    line-height: 1.32;
    padding: 8px 10px;
    text-align: justify;
  }
  .copy p + p { margin-top: 6px; }
  .copy ul { list-style: none; padding-left: 18px; }
  .copy li { line-height: 1.3; }
  .caption { font-size: 5.5px; line-height: 1.3; padding: 4px 10px; color: var(--body-light); }
  /* services panel */
  .services { background: var(--salmon); color: var(--paper); flex: 1; padding: 8px 10px; font-size: 6.2px; line-height: 1.32; }
  .services .intro { margin-bottom: 8px; }
  .service { display: flex; gap: 4px; margin-bottom: 7px; }
  .service::before { content: ""; width: 3px; height: 3px; margin-top: 2px; background: var(--paper); flex-shrink: 0; }
  .service b { font-weight: normal; color: var(--charcoal-deep); }
  /* cover panel */
  .tagline-top {
    font-family: "Comfortaa", sans-serif;
    font-weight: 700;
    color: var(--paper);
    text-align: center;
    font-size: 11px;
    line-height: 1.35;
    margin-top: 36px;
    letter-spacing: .3px;
  }
  .brand {
    margin: 54px auto 0;
    display: flex;
    flex-direction: column;
    align-items: center;
    gap: 6px;
  }
  .brand-mark { width: 18px; height: 18px; background: var(--salmon); }
  .brand-name {
    font-family: "Questrial", sans-serif;
    color: var(--salmon);
    font-size: 15px;
    text-align: center;
  }
  .brand-line { font-size: 5.5px; color: var(--salmon); text-align: center; }
  .call {
    margin-top: auto;
    margin-bottom: 14px;
    text-align: center;
    font-family: "Comfortaa", sans-serif;
    font-weight: 700;
    color: var(--paper);
    font-size: 10px;
    line-height: 1.25;
  }
  .cover-photo { position: relative; height: 232px; }
  .mini-brand {
    position: absolute; left: 10px; top: 12px;
    display: flex; align-items: center; gap: 4px;
    font-size: 7px; color: var(--paper);
  }
  .mini-brand .brand-mark { width: 8px; height: 8px; background: var(--paper); }
  .headline {
    flex: 1;
    background: var(--salmon);
    padding: 18px 14px;
    font-family: "Comfortaa", sans-serif;
    font-weight: 700;
    color: var(--paper);
    font-size: 15px;
    line-height: 1.05;
    letter-spacing: .3px;
  }
  .headline .accent { color: var(--teal); font-size: 18px; }
  .headline .big { font-size: 18px; }
</style>
</head>
<body>

<!-- Inside spread -->
<section class="spread spread--inside">
  <div class="panel">
    <div class="copy">
      <p>We provide in-home services ranging from light housekeeping to personal care and skilled nursing. We strive to give compassionate, dependable care of the highest quality while maintaining extremely competitive rates. Everything we do is geared toward meeting the individual needs of our clients. Whether you need a little help or a lot of help, you'll find that Brantley Homecare services are a cut above the rest. The Brantley Way is special: it's compassionate, professional, dependable, and flexible.</p>
      <p>All of our Care Professionals:</p>
      <ul>
        <li>Are bonded, insured, and supervised</li>
        <li>Have passed both criminal and abuse background checks</li>
        <li>Have been screened for TB</li>
        <li>Are certified in CPR and First Aid</li>
      </ul>
      <p>All client care is supervised by a Licensed Nurse Care Consultant whose duties include:</p>
      <ul>
        <li>Regular home visits</li>
        <li>Client evaluation</li>
        <li>Care Professional supervision</li>
        <li>Revising/updating client care plans</li>
        <li>24/7 on-call support</li>
      </ul>
    </div>
    <div class="photo photo--warm" style="height:76px;margin-top:auto" role="img" aria-label="Photo: caregiver holding the hands of an elderly client"></div>
    <p class="caption">Brantley Homecare is a licensed private duty home care agency proudly serving our island community.</p>
  </div>

  <div class="panel">
    <div class="photo photo--warm" style="height:90px" role="img" aria-label="Photo: nurse chatting with a smiling older man"></div>
    <div class="services">
      <p class="intro">Brantley Homecare offers four different levels of care. Our Nurse Care Consultant visits each client and family to find the right level of care during a free consultation.</p>
      <p class="service"><span><b>Quick Visit Care</b> – Our caregivers visit for short periods to help with bathing, meals and errands.</span></p>
      <p class="service"><span><b>Skilled Nursing Care</b> – Licensed nurses provide wound care, medication support and health monitoring at home.</span></p>
      <p class="service"><span><b>Private Duty Services</b> – Caregivers stay for longer shifts, offering companionship and daily living support.</span></p>
      <p class="service"><span><b>Transportation Services</b> – We drive clients safely to appointments, shopping and social outings.</span></p>
      <p>Call us to schedule your free consultation and see the difference personal care makes.</p>
    </div>
  </div>

  <div class="panel">
    <div class="copy">
      <p>Lorem ipsum dolor sit amet, consectetur adipisicing elit, sed do eiusmod tempor incididunt ut labore et dolore magna aliqua. Ut enim ad minim veniam, quis nostrud exercitation ullamco laboris nisi ut aliquip ex ea commodo consequat. Duis aute irure dolor in reprehenderit in voluptate velit esse cillum dolore eu fugiat nulla pariatur. Excepteur sint occaecat cupidatat non proident, sunt in culpa qui officia deserunt mollit anim id est laborum. Lorem ipsum dolor sit amet, consectetur adipisicing elit, sed do eiusmod tempor incididunt ut labore et dolore magna aliqua. Ut enim ad minim veniam, quis nostrud exercitation ullamco laboris nisi ut aliquip ex ea commodo consequat. Duis aute irure dolor in reprehenderit in voluptate velit esse cillum dolore eu fugiat nulla pariatur.</p>
      <p>Lorem ipsum dolor sit amet, consectetur adipisicing elit, sed do eiusmod tempor incididunt ut labore et dolore magna aliqua. Ut enim ad minim veniam, quis nostrud exercitation ullamco laboris nisi ut aliquip ex ea commodo consequat.</p>
    </div>
    <div class="photo photo--cool" style="height:112px;margin-top:auto" role="img" aria-label="Photo: doctor talking with an elderly patient"></div>
  </div>
</section>

<!-- Outside spread -->
<section class="spread spread--outside">
  <div class="panel">
    <div class="photo photo--warm" style="height:124px" role="img" aria-label="Photo: caregiver embracing an elderly client"></div>
    <div class="copy">
      <p>Lorem ipsum dolor sit amet, consectetur adipisicing elit, sed do eiusmod tempor incididunt ut labore et dolore magna aliqua. Ut enim ad minim veniam, quis nostrud exercitation ullamco laboris nisi ut aliquip ex ea commodo consequat. Duis aute irure dolor in reprehenderit in voluptate velit esse cillum dolore eu fugiat nulla pariatur. Excepteur sint occaecat cupidatat non proident, sunt in culpa qui officia deserunt mollit anim id est laborum. Lorem ipsum dolor sit amet, consectetur adipisicing elit, sed do eiusmod tempor incididunt ut labore et dolore magna aliqua. Ut enim ad minim veniam, quis nostrud exercitation ullamco laboris nisi ut aliquip ex ea commodo consequat. Duis aute irure dolor in reprehenderit in voluptate velit esse cillum dolore eu fugiat nulla pariatur.</p>
      <p>Lorem ipsum dolor sit amet, consectetur adipisicing elit, sed do eiusmod tempor incididunt ut labore et dolore magna aliqua. Ut enim ad minim veniam, quis nostrud exercitation ullamco laboris nisi ut aliquip ex ea commodo consequat.</p>
    </div>
  </div>

  <div class="panel">
    <p class="tagline-top">someone you<br>can depend on</p>
    <div class="brand">
      <span class="brand-mark"></span>
      <span class="brand-name">Brantley Homecare</span>
      <span class="brand-line">Personal care in the comfort of home</span>
    </div>
    <p class="call">CALL<br>555-014-2290</p>
  </div>

  <div class="panel">
    <div class="photo photo--portrait cover-photo" role="img" aria-label="Photo: smiling caregiver hugging an elderly woman from behind">
      <div class="mini-brand"><span class="brand-mark"></span><span>Brantley Homecare</span></div>
    </div>
    <h1 class="headline">
      it's nice<br>
      <span class="accent">to know</span><br>
      i'm taking<br>
      <span class="big">care off</span>
    </h1>
  </div>
</section>

</body>
</html>
```